Brom Vela CEO and Partners Business Card

We need a fresh, fun, simple and clean business card design....we would like a template where we can add a name and title (as well as specific email addresses). We are open to different looks (full logo on one side and a small logo on the company info side, or our logo is in the background but faint on one side but full on the other, or something else cool :-) ). Our colors are in our logo: blue, black and white...however we are not opposed to the use of other colors if it works. We build sets, make props and a host of other things for the film and television industry...our card should reflect creativity, style and professionalism.

A white background would be preferred.

I would like to see an option with Facebook and Instagram icons.

Facebook- facebook.com/bromvelaqt
Instagram- brom_vela

Our website is bromvela-example.com.

Brom Vela, Inc.
4168 Tolliver Crescent, Unit 9
Fenwick Hills, California 90000
555.210.4872 | tel
555.210.6391 | fax
www.BromVela-example.com

Sample Name and Title #1:

Curtis Welbore
CEO / Co-Owner
555.210.4872 | tel
555.210.6391 | fax
curtis@bromvela-example.com
www.BromVela-example.com

Target Market(s)

Marketing Professionals, Production Designers, Interior Designers, Film Producers, Directors, Art Directors, Event Directors

Industry/Entity Type

Entertainment Industry

Contact Information for Business Card

Curtis Welbore
CEO / Co-Owner
555.210.4872 | tel
555.210.6391 | fax
curtis@bromvela-example.com
www.BromVela-example.com

Font styles to use
Sans Serif

Colors
33a6d7
ffffff
1b1b1b

Requirements
Must have
• Logo, All Contact Info, White Background. Symmetry.
Nice to have
• Facebook and Instagram icons with addresses
• Facebook- facebook.com/bromvelaqt
• Instagram- brom_vela

```html
<!DOCTYPE html>
<html lang="en">
<head>
<meta charset="utf-8">
<title>Brom Vela CEO and Partners Business Card</title>
<link rel="stylesheet" href="https://fonts.googleapis.com/css2?family=Roboto:wght@300;400;500;900&display=swap">
<style>
  :root {
    --brand-blue: #33a6d7;
    --ink: #1b1b1b;
    --paper: #ffffff;
    --muted: #555555;
    --backdrop: #e6e6e6;
  }
  * { margin: 0; padding: 0; box-sizing: border-box; }
  html, body {
    width: 1200px; height: 987px; overflow: hidden;
    background: var(--backdrop);
    font-family: "Roboto", sans-serif;
  }
  .card {
    position: absolute; left: 293px; width: 615px; height: 352px;
  }
  .card--front { top: 130px; background: var(--paper); color: var(--ink); }
  .card--back { top: 505px; background: #000; color: var(--paper); }

  .wordmark {
    position: absolute; left: 0; right: 0;
    display: flex; justify-content: center; align-items: center; gap: 14px;
    font-weight: 900; font-size: 66px; letter-spacing: -1px; line-height: 1;
  }
  .wordmark__dot {
    width: 22px; height: 22px; border-radius: 50%; background: var(--brand-blue);
  }
  .card--front .wordmark { top: 50px; color: var(--ink); }
  .card--back .wordmark { top: 132px; color: var(--paper); }

  .name-rule {
    position: absolute; top: 172px; left: 29px; right: 31px;
    display: flex; align-items: center; gap: 4px;
    white-space: nowrap;
  }
  .name-rule::before, .name-rule::after {
    content: ""; flex: 1; height: 1px; background: var(--ink);
  }
  .name-rule__name { color: var(--brand-blue); font-size: 19px; font-weight: 500; }
  .name-rule__title { font-size: 15px; font-weight: 400; }

  .contact-list {
    position: absolute; top: 215px; left: 33px; list-style: none;
    color: var(--muted); font-size: 15px; font-weight: 300;
  }
  .contact-list li { display: flex; align-items: center; gap: 8px; height: 23.5px; }
  .contact-list svg { width: 15px; height: 14px; fill: var(--brand-blue); }

  .address {
    position: absolute; top: 222px; right: 38px; text-align: right;
    color: var(--muted); font-size: 15px; font-weight: 300; line-height: 20.5px;
    font-style: normal;
  }
  .footer-rule {
    position: absolute; top: 299px; left: 29px; right: 31px; height: 1px; background: var(--ink);
  }
  .website {
    position: absolute; top: 311px; left: 0; right: 0; text-align: center;
    color: var(--brand-blue); font-size: 14px; letter-spacing: 0.42em; font-weight: 400;
  }

  .social {
    position: absolute; top: 277px; left: 0; right: 0;
    display: flex; justify-content: center; gap: 14px;
    font-size: 15px; font-weight: 300;
  }
  .social__item { display: flex; align-items: center; gap: 6px; }
  .social__badge { width: 24px; height: 24px; border-radius: 50%; background: var(--paper); }
</style>
</head>
<body>
  <section class="card card--front" aria-label="Business card front">
    <div class="wordmark"><span>Brom Vela</span><span class="wordmark__dot"></span></div>

    <h1 class="name-rule">
      <span class="name-rule__name">Curtis Welbore -</span>
      <span class="name-rule__title">CEO / Co-Owner</span>
    </h1>

    <ul class="contact-list">
      <li>
        <svg viewBox="0 0 16 14" aria-hidden="true"><path d="M1 3c0-2 3-3 7-3s7 1 7 3v1h-4V3H5v1H1z"/><path d="M3 6h10l2 7H1z"/><circle cx="8" cy="9.5" r="2" fill="#fff"/></svg>
        555.210.4872
      </li>
      <li>
        <svg viewBox="0 0 16 14" aria-hidden="true"><rect x="4" y="0" width="8" height="5"/><rect x="1" y="5" width="14" height="6" rx="1"/><rect x="4" y="10" width="8" height="4"/></svg>
        555.210.6391
      </li>
      <li>
        <svg viewBox="0 0 16 14" aria-hidden="true"><path d="M0 2h16v10H0z"/><path d="M0 2l8 6 8-6" fill="none" stroke="#fff" stroke-width="1.3"/></svg>
        curtis@bromvela-example.com
      </li>
    </ul>

    <address class="address">
      4168 Tolliver Crescent<br>
      Unit 9, Fenwick Hills<br>
      California 90000
    </address>

    <div class="footer-rule"></div>
    <p class="website">www.BromVela-example.com</p>
  </section>

  <section class="card card--back" aria-label="Business card back">
    <div class="wordmark"><span>Brom Vela</span><span class="wordmark__dot"></span></div>
    <div class="social">
      <span class="social__item"><span class="social__badge"></span>bromvelaqt</span>
      <span class="social__item"><span class="social__badge"></span>brom_vela</span>
    </div>
  </section>
</body>
</html>
```